Business Card Design

I have two logos , one is for the front of the card and the other for the back. The front image is the road and the sun, the back image should be the atom with the motto at the bottom. The back of the card should be black with the atom and lettering white. The front should have the image with the road and lettering black with the yellow sun all on a white background.
Updates

I have changed what I would like done. The only logo I want to use is the atom logo. White lettering with a black background on the front and back of the card. There should be no contact info on the back of the card. On the back there should b the logo with company name and the slogan underneath at the bottom of the card, also on the back if you can have the logo  image in the background as well in a gray or silver can be tiled or cascade of some sort.

On the front it should have all of the contact info with an email address added  tarnvista@quellmail.net   Black background with white lettering and another larger image of the logo in a gray or silver in the background. The logo and name side by side with the slogan directly under the name.

Industry/Entity Type

Business

Contact Information for Business Card

Colin Marsh
Director of Operations
8162 Pemberly Ln #417
Georgetown, TX 78633
Cell: (512)804-3176
Fax: (512)471-0852

```html
<!DOCTYPE html>
<html lang="en">
<head>
<meta charset="utf-8">
<title>Pecos Mobile Imaging — Business Cards</title>
<link rel="stylesheet" href="https://fonts.googleapis.com/css2?family=Varela+Round&family=Lato:wght@300;400&display=swap">
<style>
  :root {
    --page: #ffffff;
    --card: #000000;
    --ink: #ffffff;
    --ink-soft: #e6e6e6;
    --silver: #3a3a3c;
    --silver-faint: #262628;
    --shadow: rgba(0, 0, 0, 0.55);
  }
  * { margin: 0; padding: 0; box-sizing: border-box; }
  html, body {
    width: 1200px; height: 1000px; overflow: hidden;
    background: var(--page);
  }
  .canvas { position: relative; width: 1200px; height: 1000px; }

  .card {
    position: absolute; left: 212px; width: 776px; height: 442px;
    background: var(--card); color: var(--ink);
    font-family: "Varela Round", sans-serif;
    box-shadow: 0 4px 10px var(--shadow);
    overflow: hidden;
  }
  .card--front { top: 50px; }
  .card--back { top: 513px; }

  .bg-mark {
    position: absolute; border-radius: 50%;
    border: 18px solid var(--silver);
  }
  .card--front .bg-mark { left: 470px; top: 60px; width: 380px; height: 380px; }
  .card--back .bg-mark { left: 218px; top: -40px; width: 340px; height: 340px; border-color: var(--silver-faint); }

  .brand {
    position: absolute; display: flex; align-items: center; gap: 34px;
  }
  .brand-mark {
    width: 102px; height: 102px; flex: none;
    border: 6px solid var(--ink); border-radius: 50%;
  }
  .brand-name { font-size: 33px; line-height: 1; white-space: nowrap; }

  .card--front .brand { left: 120px; top: 32px; }

  .slogan { font-size: 20px; word-spacing: 6px; white-space: nowrap; }
  .card--front .slogan {
    position: absolute; left: 0; right: 0; top: 190px; text-align: center;
  }

  .contact {
    position: absolute; left: 0; right: 0; top: 262px; text-align: center;
    font-size: 20px; line-height: 29px; letter-spacing: 0.3px;
  }
  .contact .person { font-size: 21px; }
  .contact .detail { font-family: "Lato", sans-serif; font-weight: 300; color: var(--ink-soft); }
  .contact .label { font-family: "Varela Round", sans-serif; color: var(--ink); }

  .card--back .brand { left: 120px; top: 270px; }
  .card--back .brand-text { display: flex; flex-direction: column; gap: 14px; }
  .card--back .slogan { padding-left: 2px; }
</style>
</head>
<body>
<main class="canvas">

  <section class="card card--front" aria-label="Front of business card">
    <div class="bg-mark" aria-hidden="true"></div>
    <div class="brand">
      <div class="brand-mark" aria-hidden="true"></div>
      <div class="brand-name">Pecos Mobile Imaging</div>
    </div>
    <p class="slogan">Professional Timely Accurate</p>
    <div class="contact">
      <p class="person">Colin Marsh</p>
      <p class="detail">Director of Operations</p>
      <p class="detail">8162 Pemberly Ln #417 Georgetown, TX 78633</p>
      <p class="detail"><span class="label">Cell:</span> (512)804-3176&nbsp;&nbsp;<span class="label">Fax:</span> (512)471-0852</p>
      <p class="detail">tarnvista@quellmail.net</p>
    </div>
  </section>

  <section class="card card--back" aria-label="Back of business card">
    <div class="bg-mark" aria-hidden="true"></div>
    <div class="brand">
      <div class="brand-mark" aria-hidden="true"></div>
      <div class="brand-text">
        <div class="brand-name">Pecos Mobile Imaging</div>
        <p class="slogan">Professional Timely Accurate</p>
      </div>
    </div>
  </section>

</main>
</body>
</html>
```